The company Velquist needs a design for CBD capsules

We (Velquist) need a new design for our CBD capsules. We already have a design for CBD oil. However, we do not want to use this completely. The Talmbex label and the cans serve as a template. Please upload in the format 139mm x 59mm incl.
2mm bleed all around and in .pdf vector. The logo files for Velquist are included in the briefing.

Industry/Entity Type

Onlineshop

Colors
00AB8E
00BBA5
67D7C9
C6EFE9
E9F9F6

Requirements
Must have
• Please in the format 139mm x 59mm incl. 2mm bleed all around and .pdf vector
Should not have
• It shouldn't be the same label, but it should be recognizable.

```html
<!DOCTYPE html>
<html lang="de">
<head>
<meta charset="utf-8">
<title>Velquist CBD Premium Kapseln – Etikett</title>
<link rel="stylesheet" href="https://fonts.googleapis.com/css2?family=Jost:wght@500;600;700&family=Open+Sans:wght@700;800&display=swap">
<style>
  :root {
    --stage: #0b0b0b;
    --green-deep: #009a80;
    --green: #00ab8e;
    --green-light: #00bba5;
    --mint: #67d7c9;
    --navy: #15304a;
    --silver: #dedfe1;
    --silver-dark: #c3c6c9;
    --band-text: #0a9a7c;
  }
  * { margin: 0; padding: 0; box-sizing: border-box; }
  html, body { width: 1200px; height: 1200px; overflow: hidden; background: var(--stage); }
  .label {
    position: absolute; left: 170px; top: 97px; width: 860px; height: 1006px;
    background: linear-gradient(100deg, var(--green-deep) 0%, var(--green-light) 45%, var(--green) 70%, var(--green-deep) 100%);
    font-family: "Jost", sans-serif;
  }
  .leaf-decor {
    position: absolute; inset: 0 0 195px 0;
    background: radial-gradient(ellipse at 30% 45%, rgba(103,215,201,0.25), transparent 55%),
                radial-gradient(ellipse at 80% 30%, rgba(103,215,201,0.18), transparent 50%);
  }
  .brand {
    position: absolute; left: 0; right: 0; top: 92px; text-align: center;
    font-weight: 700; font-size: 124px; line-height: 1; color: var(--navy); letter-spacing: -1px;
  }
  .product {
    position: absolute; left: 0; right: 0; top: 290px; text-align: center;
    font-family: "Jost", sans-serif; font-weight: 600; font-size: 372px; line-height: 1;
    color: var(--silver); letter-spacing: 4px;
  }
  .subtitle {
    position: absolute; left: 0; right: 0; top: 632px; text-align: center;
    font-family: "Open Sans", sans-serif; font-weight: 700; font-size: 60px; line-height: 1;
    color: var(--silver); letter-spacing: 2px;
  }
  .contents {
    position: absolute; left: 0; right: 0; top: 752px; text-align: center;
    font-family: "Open Sans", sans-serif; font-weight: 800; font-size: 46px; line-height: 1; color: var(--navy);
  }
  .contents .small { font-size: 32px; }
  .feature-band {
    position: absolute; left: 0; right: 0; bottom: 0; height: 195px;
    background: linear-gradient(100deg, var(--silver-dark), #eeeff0 45%, var(--silver) 70%, var(--silver-dark));
  }
  .feature {
    position: absolute; top: 26px; transform: translateX(-50%);
    display: flex; flex-direction: column; align-items: center; gap: 12px;
  }
  .feature svg { width: 76px; height: 76px; }
  .feature span { font-weight: 600; font-size: 26px; color: var(--band-text); white-space: nowrap; }
</style>
</head>
<body>
<div class="label">
  <div class="leaf-decor" role="img" aria-label="Faint hemp leaf pattern in soft green tones"></div>
  <div class="brand">Velquist</div>
  <div class="product">CBD</div>
  <div class="subtitle">PREMIUM KAPSELN</div>
  <div class="contents">60 KAPSELN <span class="small">NET. WT</span> 58<span class="small">G</span></div>

  <div class="feature-band">
    <div class="feature" style="left:133px">
      <svg viewBox="0 0 80 80"><path d="M14 18 L30 70 L40 70 L26 20 Z M40 70 C40 40 50 24 66 14 C68 40 58 60 40 70 Z" fill="var(--green)"/></svg>
      <span>Vegan</span>
    </div>
    <div class="feature" style="left:242px">
      <svg viewBox="0 0 80 80" fill="none" stroke="var(--green)" stroke-width="7"><path d="M18 8 H62 M18 72 H62 M22 10 C22 36 58 44 58 70 M58 10 C58 36 22 44 22 70"/><path d="M30 24 H50 M30 56 H50" stroke-width="5"/></svg>
      <span>Non-GM</span>
    </div>
    <div class="feature" style="left:388px">
      <svg viewBox="0 0 80 80" fill="var(--green)"><path d="M40 16 C50 28 50 44 40 52 C30 44 30 28 40 16 Z"/><path d="M6 52 C20 42 34 46 38 60 C24 66 12 62 6 52 Z"/><path d="M74 52 C60 42 46 46 42 60 C56 66 68 62 74 52 Z"/></svg>
      <span>Gluten-Free</span>
    </div>
    <div class="feature" style="left:547px">
      <svg viewBox="0 0 80 80"><circle cx="40" cy="40" r="34" fill="var(--green)"/></svg>
      <span>Kosher</span>
    </div>
    <div class="feature" style="left:691px">
      <svg viewBox="0 0 80 80"><path d="M14 34 a8 8 0 1 1 8 -8 L58 34 a8 8 0 1 1 8 8 a8 8 0 1 1 -8 8 L22 42 a8 8 0 1 1 -8 -8 Z" fill="var(--green)"/><path d="M62 6 L20 76" stroke="var(--navy)" stroke-width="3"/></svg>
      <span>Gelatin-Free</span>
    </div>
  </div>
</div>
</body>
</html>
```